Maison Vurel

menu design, menu change,
will send hand written rough draft soon
Updates

Project Deadline Extended
Reason: Got off to a slow start. Things are progressing now. Thank you.

Target Market(s)

18-60 yr olds, blue collar & professionals, middle class, median income, families,upscale - casual- steakhouse concept

Industry/Entity Type

Restaurant

Colors
f68d4c
f37122
f78f20
faa54b
ffc214
fece3e
fbee3e
fbed22
333333

Requirements
Must have
• Front cover, back cover. 2 inside views
Nice to have
• 8 x 14 page size

```html
<!DOCTYPE html>
<html lang="en">
<head>
<meta charset="utf-8">
<title>Maison Vurel — Menu</title>
<link rel="stylesheet" href="https://fonts.googleapis.com/css2?family=Playball&family=Francois+One&family=Alfa+Slab+One&family=Oswald:wght@500;600&family=Crimson+Text:ital@1&display=swap">
<style>
  :root{
    --board:#262626;
    --board-light:#333333;
    --wood:#6b4327;
    --wood-dark:#4a2c18;
    --chalk:#f2f0ea;
    --chalk-soft:#d9d6cf;
    --orange:#f37122;
    --orange-warm:#f78f20;
    --yellow:#ffc214;
    --yellow-line:#fbed22;
    --cream:#f6e6b8;
    --stage:#f1f1f1;
  }
  *{box-sizing:border-box;margin:0;padding:0}
  html,body{width:1200px;height:1058px;overflow:hidden}
  body{background:linear-gradient(#ffffff,var(--stage));position:relative;font-family:"Crimson Text",serif}

  .page{position:absolute;top:77px;width:661px;height:1156px;transform:scale(.8);transform-origin:0 0;
    background:linear-gradient(90deg,var(--wood-dark),var(--wood) 50%,var(--wood-dark));overflow:hidden;color:var(--chalk)}
  .page--steak{left:59px}
  .page--chicken{left:615px}
  .board{position:absolute;left:31px;top:0;width:600px;height:1156px;
    background:radial-gradient(ellipse at 50% 40%,var(--board-light),var(--board) 75%)}
  .chalk-edge{position:absolute;top:164px;bottom:10px;width:6px;
    background:repeating-linear-gradient(180deg,var(--chalk-soft) 0 2px,transparent 2px 5px);opacity:.7}
  .sketch-band{position:absolute;left:31px;top:0;width:600px;height:150px;
    background:linear-gradient(180deg,#3b3b3b,#2d2d2d 80%,rgba(38,38,38,0))}

  .script-title{position:absolute;left:31px;width:600px;text-align:center;font-family:"Playball",cursive;font-weight:400;color:var(--cream);white-space:nowrap}
  .title-rule{position:absolute;top:160px;height:6px;width:83px;
    background:repeating-linear-gradient(90deg,var(--chalk-soft) 0 2px,transparent 2px 5px);opacity:.8}
  .tagline{position:absolute;left:31px;width:600px;text-align:center;font-family:"Oswald",sans-serif;font-weight:600;color:var(--yellow);font-size:18px;line-height:20px;white-space:nowrap}
  .hair{position:absolute;height:1px;background:rgba(242,240,234,.35)}
  .divider{position:absolute;left:332px;width:1px;background:rgba(242,240,234,.35)}

  .c-l,.c-r{position:absolute;text-align:center;width:290px}
  .c-l{left:41px}
  .c-r{left:330px}
  .item-name{font-family:"Francois One",sans-serif;font-size:20px;line-height:24px;letter-spacing:1px;text-transform:uppercase;color:var(--chalk);white-space:nowrap}
  .item-desc{font-style:italic;font-size:13px;line-height:16.5px;color:var(--chalk-soft);white-space:nowrap}

  .price{position:absolute;width:200px;height:30px;line-height:30px;text-align:center;
    background:linear-gradient(90deg,var(--orange-warm),var(--orange));
    clip-path:polygon(0 30%,8% 8%,6% 0,55% 4%,92% 0,100% 20%,94% 45%,100% 62%,95% 90%,72% 100%,30% 96%,4% 100%,7% 72%,0 56%);
    font-family:"Alfa Slab One",serif;font-size:22px;color:#fff}
  .p-l{left:86px}
  .p-r{left:375px}
  .price--cut{font-family:"Oswald",sans-serif;font-weight:500;font-size:21px}
  .price--small{height:24px;line-height:24px;font-size:19px}
  .price--side{width:190px;left:91px;height:26px;line-height:26px;font-size:19px}

  .side-name{font-family:"Francois One",sans-serif;font-size:14px;line-height:16px;letter-spacing:.8px;text-transform:uppercase;color:var(--chalk);white-space:nowrap}
  .potato-list{position:absolute;left:330px;width:290px;top:796px;text-align:center;list-style:none}
  .potato-list li{font-family:"Francois One",sans-serif;font-size:16px;line-height:38px;letter-spacing:.8px;text-transform:uppercase}

  .note{position:absolute;font-style:italic;font-size:14px;line-height:18px;color:var(--chalk-soft);white-space:nowrap}
  .yellow-rule{position:absolute;height:3px;background:var(--yellow-line);opacity:.9}

  .footer-address,.footer-contact{position:absolute;top:1096px;font-size:12.5px;line-height:15px;font-style:italic;color:var(--chalk-soft);white-space:nowrap}
  .footer-address{left:72px}
  .footer-contact{left:463px}
  .call-out{position:absolute;left:226px;width:200px;text-align:center;font-family:"Francois One",sans-serif;font-size:14px;line-height:16px;letter-spacing:.6px;top:1090px}
  .call-number{position:absolute;left:201px;width:250px;top:1106px;text-align:center;font-family:"Oswald",sans-serif;font-weight:600;font-size:24px;line-height:28px;color:var(--yellow)}
</style>
</head>
<body>

<section class="page page--steak">
  <div class="board"></div>
  <div class="sketch-band" role="img" aria-label="Chalk sketch of vegetables, herbs, shellfish and fish along the top edge"></div>
  <div class="chalk-edge" style="left:41px"></div>
  <div class="chalk-edge" style="left:613px"></div>
  <div class="title-rule" style="left:38px"></div>
  <div class="title-rule" style="left:538px"></div>
  <h1 class="script-title" style="top:129px;font-size:48px;line-height:60px">This is Cattle Country!</h1>
  <p class="tagline" style="top:192px">ALL SERVED WITH CHOICE OF POTATO + HOT BREAD</p>
  <div class="hair" style="left:86px;width:490px;top:219px"></div>
  <div class="divider" style="top:235px;height:405px"></div>

  <h2 class="c-l item-name" style="top:242px">Chicken Fried Steak</h2>
  <p class="c-l item-desc" style="top:268px">Hand breaded and served with country gravy</p>
  <span class="price p-l" style="top:295px">$12.99</span>

  <h2 class="c-l item-name" style="top:353px">Parmesan Pepper<br>Press Steak</h2>
  <p class="c-l item-desc" style="top:406px">12oz choice tenderloin cut, char breaded &amp;<br>coated with a parmesan pepper crust</p>
  <span class="price p-l" style="top:451px">$19.99</span>

  <h2 class="c-l item-name" style="top:509px;font-size:21px">Steak Chateaubriand</h2>
  <p class="c-l item-desc" style="top:538px">12oz choice tenderloin cut, drizzled with a<br>parmesan cream sauce &amp; complimented<br>with grilled asparagus spears</p>
  <span class="price p-l" style="top:595px">$19.99</span>

  <h2 class="c-r item-name" style="top:241px;line-height:21px">Mushroom Ground<br>Shallow Steak</h2>
  <p class="c-r item-desc" style="top:289px;font-size:12px;line-height:15px">14oz ground shallow smothered with<br>best mushroom gravy</p>
  <span class="price p-r" style="top:324px">$12.99</span>

  <h2 class="c-r item-name" style="top:367px">Steak Del Rio</h2>
  <p class="c-r item-desc" style="top:397px">12oz choice tenderloin cut rubbed with bold<br>south western spices, flame boiled tapped<br>with chili pepper butter and fried onion<br>tangled</p>
  <span class="price p-r" style="top:470px">$19.99</span>

  <h2 class="c-r item-name" style="top:514px">Boston Bleu Cheese<br>Steak</h2>
  <p class="c-r item-desc" style="top:566px">12oz choice tenderloin cut,flamed boiled,<br>tapped with melting bleu cheese crumbles</p>
  <span class="price p-r" style="top:605px">$19.99</span>

  <h1 class="script-title" style="top:669px;font-size:34px;line-height:40px">Maison Vurel Premium Steak Selection</h1>
  <p class="tagline" style="top:721px">CHOICE AND PRIME GRADE BEEF</p>
  <p class="tagline" style="top:744px;font-weight:500">SERVED WITH HOUSE SALAD, CHOICE OF POTATO AND HOT BREAD</p>
  <div class="hair" style="left:86px;width:490px;top:770px"></div>
  <div class="divider" style="top:790px;height:270px"></div>

  <h2 class="c-l item-name" style="top:788px">Filet Mignow</h2>
  <p class="c-l item-desc" style="top:816px">Bacon wrapped. Most tender cut</p>
  <span class="price p-l price--cut" style="top:838px">8oz-$24.99</span>
  <span class="price p-l price--cut" style="top:871px">10oz-$28.99</span>

  <h2 class="c-l item-name" style="top:923px">Kansas City Strip</h2>
  <p class="c-l item-desc" style="top:952px">Firmer texture, full of flavor</p>
  <span class="price p-l price--cut" style="top:977px">16oz-$26.99</span>

  <h2 class="c-r item-name" style="top:788px">Rib Eye Steak</h2>
  <p class="c-r item-desc" style="top:816px">Well marble, rich, full of flavor cut<br>from the prime rib</p>
  <span class="price p-r price--cut" style="top:854px">15oz-$28.99</span>

  <h2 class="c-r item-name" style="top:903px">Beef Tenderloin<br>Kabob</h2>
  <p class="c-r item-desc" style="top:956px">8oz beef tenderloin, skewered with bell<br>pepper ,onion, tomato, mushrooms, pineapple<br>and drizzled with light Italian marinade</p>
  <span class="price p-r" style="top:1015px">$26.99</span>

  <div class="yellow-rule" style="left:166px;width:220px;top:1073px"></div>
  <p class="footer-address">48 Harlan Avenue, Brookfield<br>Ohio, USA 44403</p>
  <p class="call-out">CALL OUT</p>
  <p class="call-number">+1 330 555 0142</p>
  <p class="footer-contact">Phone : +1 330 555 0198<br>Email : hello@maisonvurel.com</p>
</section>

<section class="page page--chicken">
  <div class="board"></div>
  <div class="sketch-band" role="img" aria-label="Chalk sketch of vegetables, herbs, shellfish and fish along the top edge"></div>
  <div class="chalk-edge" style="left:41px"></div>
  <div class="chalk-edge" style="left:613px"></div>
  <div class="title-rule" style="left:38px"></div>
  <div class="title-rule" style="left:538px"></div>
  <h1 class="script-title" style="top:129px;font-size:48px;line-height:60px">Chicken And Seafood</h1>
  <p class="tagline" style="top:192px">SERVED WITH CHOICE OF POTATO AND HOT BREAD</p>
  <div class="hair" style="left:86px;width:490px;top:219px"></div>
  <div class="divider" style="top:235px;height:830px"></div>

  <h2 class="c-l item-name" style="top:242px">Charbroiled<br>Chicken Breast</h2>
  <p class="c-l item-desc" style="top:293px">10oz flamed broiled breast</p>
  <span class="price p-l" style="top:315px">$14.99</span>

  <h2 class="c-l item-name" style="top:355px">Chicken Fried<br>Chicken Breast</h2>
  <p class="c-l item-desc" style="top:405px">10oz hand breaded breast, fried, served with a<br>corn on the cob, mashed potato and country gravy</p>
  <span class="price p-l" style="top:444px">$14.99</span>

  <h2 class="c-l item-name" style="top:484px">Hand Breaded<br>Chicken Strips</h2>
  <p class="c-l item-desc" style="top:533px">Cut and breaded per order</p>
  <span class="price p-l" style="top:554px">$9.99</span>

  <h2 class="c-l item-name" style="top:599px">Chicken Ka-Bob</h2>
  <p class="c-l item-desc" style="top:629px">10oz charbroiled Breast, skewered with bell<br>peppers, onion, mushrooms, tomato, pineap-<br>ples and drizzled with light Italian marinade</p>
  <span class="price p-l" style="top:684px">$19.99</span>

  <h2 class="c-r item-name" style="top:241px;line-height:21px">North Atlantic<br>Salmon</h2>
  <p class="c-r item-desc" style="top:287px;font-size:12px">Charbroiled fillet</p>
  <span class="price p-r price--cut price--small" style="top:308px">8oz - $19.99</span>

  <h2 class="c-r item-name" style="top:346px">English Style Cod</h2>
  <p class="c-r item-desc" style="top:370px">House battered Icelandic cod loin</p>
  <span class="price p-r" style="top:391px">$17.99</span>

  <h2 class="c-r item-name" style="top:434px;font-size:19px">Deep Fried Gulf Shrimp</h2>
  <p class="c-r item-desc" style="top:460px">6 jumbo Shrimps</p>
  <span class="price p-r" style="top:480px">$17.99</span>

  <h2 class="c-r item-name" style="top:522px">Mahi Mahi</h2>
  <p class="c-r item-desc" style="top:547px">9oz charbroiled served under a shrimp &amp;<br>mushroom white sauce on a bit of steamed<br>garden vegetables</p>
  <span class="price p-r" style="top:600px">$19.99</span>

  <h2 class="c-r item-name" style="top:636px;font-size:19px">Country Fried Catfish</h2>
  <p class="c-r item-desc" style="top:662px">Catfish fillets, hand Breaded and deep fried</p>
  <span class="price p-r" style="top:687px">$12.99</span>

  <h1 class="script-title" style="left:-114px;top:731px;font-size:40px;line-height:46px">Sides</h1>
  <div class="hair" style="left:86px;width:215px;top:796px"></div>

  <p class="c-l side-name" style="top:808px">Steamed Garden Vegetables</p>
  <span class="price price--side" style="top:829px">$4.99</span>
  <p class="c-l side-name" style="top:863px">Twice Baked Potato</p>
  <span class="price price--side" style="top:884px">$4.99</span>
  <p class="c-l side-name" style="top:918px;line-height:17px">Loaded Baked and<br>Mashed Potato</p>
  <span class="price price--side" style="top:955px">$4.99</span>
  <p class="c-l side-name" style="top:987px">Grilled Asparagus</p>
  <span class="price price--side" style="top:1008px">$4.99</span>
  <p class="c-l side-name" style="top:1042px">House or Gasan Salad</p>
  <span class="price price--side" style="top:1063px">$4.99</span>
  <p class="note" style="left:91px;top:1097px">*If in place of Potato, add 2.99</p>

  <ul class="potato-list">
    <li>Potato Choice</li>
    <li>Baked</li>
    <li>Mashed</li>
    <li>American Fries</li>
    <li>German Fries</li>
    <li>French Fries</li>
    <li>Onions Rings</li>
  </ul>
  <div class="yellow-rule" style="left:341px;width:250px;top:1071px"></div>
  <p class="note" style="left:338px;top:1097px;font-size:13px">Consumer advisory : ..............................................</p>
</section>

</body>
</html>
```